label for coconut oil

A label to go on bottles of organic virgin coconut oil.
Fresh looking green stylised coconut,un cluttered,white or natural background,produce of Philipines,easy to reproduce,
will also use for other coconut products.
Portrait and landscape options.
Want it to look crafty,not to commercial,simple.
Company name is Amber Ridge but does not have to be included[can go on back of bottle with nutritional details]

```html
<!DOCTYPE html>
<html lang="en">
<head>
<meta charset="utf-8">
<title>Extra Virgin Coconut Oil Label</title>
<link rel="stylesheet" href="https://fonts.googleapis.com/css2?family=Baloo+2:wght@700&family=Signika:wght@400;500&display=swap">
<style>
  :root {
    --page: #ffffff;
    --label: #5b5538;
    --lime: #b5c424;
    --white: #ffffff;
    --leaf-light: #eef3c8;
  }
  html, body {
    margin: 0;
    padding: 0;
    width: 879px;
    height: 1200px;
    overflow: hidden;
    background: var(--page);
  }
  .canvas {
    position: relative;
    width: 879px;
    height: 1200px;
  }
  .label {
    position: absolute;
    left: 166px;
    top: 147px;
    width: 546px;
    height: 906px;
    background: var(--label);
    border-radius: 12px;
    font-family: "Signika", sans-serif;
  }
  .label-frame {
    position: absolute;
    inset: 9px;
    border: 2px solid var(--lime);
    border-radius: 8px;
  }
  .grade {
    position: absolute;
    left: 48px;
    top: 40px;
    margin: 0;
    font-family: "Signika", sans-serif;
    font-weight: 500;
    font-size: 54px;
    line-height: 1;
    color: var(--lime);
    letter-spacing: 0.5px;
  }
  .product-name {
    position: absolute;
    left: 46px;
    top: 96px;
    margin: 0;
    font-family: "Baloo 2", sans-serif;
    font-weight: 700;
    font-size: 86px;
    line-height: 1;
    color: var(--white);
    letter-spacing: -1px;
  }
  .oil-mark {
    position: absolute;
    left: 368px;
    top: 54px;
    width: 130px;
    height: 148px;
    background: linear-gradient(160deg, var(--lime) 0%, #9aa820 100%);
    border-radius: 8px;
  }
  .organic {
    position: absolute;
    left: 62px;
    top: 266px;
    width: 50px;
    height: 500px;
    display: flex;
    flex-direction: column;
    justify-content: space-between;
    align-items: center;
    margin: 0;
    font-family: "Signika", sans-serif;
    font-weight: 500;
    font-size: 64px;
    line-height: 1;
    color: var(--lime);
  }
  .palm-leaf {
    position: absolute;
    left: 151px;
    top: 246px;
    width: 358px;
    height: 504px;
    background: linear-gradient(135deg, var(--white) 0%, var(--leaf-light) 45%, var(--lime) 100%);
  }
  .origin {
    position: absolute;
    left: 34px;
    top: 830px;
    margin: 0;
    font-size: 23px;
    line-height: 1;
    color: var(--lime);
  }
  .volume {
    position: absolute;
    right: 32px;
    top: 814px;
    margin: 0;
    color: var(--white);
    line-height: 1;
    white-space: nowrap;
  }
  .volume .volume-prefix { font-size: 27px; }
  .volume .volume-amount { font-size: 40px; }
</style>
</head>
<body>
<div class="canvas">
  <section class="label">
    <div class="label-frame"></div>

    <p class="grade">extravirgin</p>
    <h1 class="product-name">Coconut</h1>

    <div class="oil-mark" role="img" aria-label="Lettered oil droplet mark reading Oil"></div>

    <p class="organic" aria-label="Organic">
      <span>O</span><span>r</span><span>g</span><span>a</span><span>n</span><span>i</span><span>c</span>
    </p>

    <div class="palm-leaf" role="img" aria-label="Stylised palm frond in white and lime green"></div>

    <p class="origin">product of the Philippines</p>
    <p class="volume"><span class="volume-prefix">net </span><span class="volume-amount">300 ml</span></p>
  </section>
</div>
</body>
</html>
```